Natural Light/Organic/Documentary Photography Business

I like a simple, approachable, feminine, earthy/organic feel. Earth/neutral tones, nothing too loud or obnoxious. I like the watercolor look. I don't want anything too trendy or something I'll get tired of after a couple months. As far as colors, I am much more a fan of cream/taupe/blue/green...not a fan of pink or purple at all.

Target Market(s)

Weddings & Families

Industry/Entity Type

Wedding Photography

Contact Information for Business Card

website, email, phone number

Font styles to use
Other font styles liked:
• Horizontes, Gotham

Colors

Designer to choose colors to be used in the design.

Requirements
Must have
• Website: www.meliskaverholt.com
• Phone: 482.319.6047
• Email: tessa@meliskaverholt.com
Nice to have
• I like the watercolor look but its not necessary. I like simple/earthy tones. Nothing too loud or distracting. Simple & feminine without being too girly. I like an approachable/soft feel.
• Instagram: www.instagram.com/meliskaverholtphotography/
Should not have
• NO loud colors or design or pattern. I do not want a photo of a camera or lens or anything cheesy like that.

```html
<!DOCTYPE html>
<html lang="en">
<head>
<meta charset="utf-8">
<title>Meliska Verholt Photography – Business Card</title>
<link rel="stylesheet" href="https://fonts.googleapis.com/css2?family=Montserrat:wght@300;400&display=swap">
<style>
  :root {
    --backdrop: #8a8a8a;
    --card: #ffffff;
    --taupe: #8c7f76;
    --icon: #a89178;
    --wash-cream: #f1ead2;
    --wash-sage: #dfe6cf;
  }
  * { margin: 0; padding: 0; box-sizing: border-box; }
  html, body { width: 1200px; height: 864px; overflow: hidden; }
  body {
    background: var(--backdrop);
    font-family: "Montserrat", sans-serif;
    color: var(--taupe);
    display: flex;
    align-items: center;
    justify-content: center;
    gap: 80px;
  }
  .card {
    position: relative;
    width: 420px;
    height: 720px;
    background: var(--card);
    border-radius: 30px;
    overflow: hidden;
    box-shadow: 0 18px 40px rgba(0,0,0,0.28);
  }
  .brand {
    position: absolute;
    left: 0; right: 0;
    top: 300px;
    text-align: center;
  }
  .brand-name {
    font-weight: 300;
    font-size: 34px;
    letter-spacing: 0.02em;
    color: var(--taupe);
  }
  .brand-tag {
    margin-top: 8px;
    font-weight: 400;
    font-size: 11px;
    letter-spacing: 0.42em;
    color: var(--taupe);
  }
  .contact {
    position: absolute;
    left: 38px;
    bottom: 40px;
    list-style: none;
  }
  .contact li {
    display: flex;
    align-items: center;
    gap: 14px;
    font-size: 15.5px;
    font-weight: 400;
    letter-spacing: 0.06em;
    line-height: 34px;
  }
  .contact svg { width: 18px; height: 18px; flex: none; fill: none; stroke: var(--icon); stroke-width: 1.8; }
  .contact svg .solid { fill: var(--icon); stroke: none; }
  .wash {
    position: absolute;
    top: 0;
    left: 0;
    width: 100%;
    height: 300px;
    background: radial-gradient(ellipse 300px 230px at 45% 0%, var(--wash-cream) 0%, var(--wash-sage) 45%, rgba(223,230,207,0) 100%);
  }
  .card-back .brand { top: 330px; }
</style>
</head>
<body>
  <section class="card card-front">
    <div class="brand">
      <div class="brand-name">Meliska Verholt</div>
      <div class="brand-tag">PHOTOGRAPHY</div>
    </div>
    <ul class="contact">
      <li>
        <svg viewBox="0 0 24 24"><path class="solid" d="M6.6 10.8c1.4 2.8 3.8 5.1 6.6 6.6l2.2-2.2c.3-.3.7-.4 1-.2 1.1.4 2.3.6 3.6.6.6 0 1 .4 1 1V20c0 .6-.4 1-1 1C10.6 21 3 13.4 3 4c0-.6.4-1 1-1h3.5c.6 0 1 .4 1 1 0 1.3.2 2.5.6 3.6.1.3 0 .7-.2 1z"/></svg>
        <span>482.319.6047</span>
      </li>
      <li>
        <svg viewBox="0 0 24 24"><rect class="solid" x="2" y="5" width="20" height="14" rx="1.5"/><path d="M3 6l9 7 9-7" stroke="#fff"/></svg>
        <span>tessa@meliskaverholt.com</span>
      </li>
      <li>
        <svg viewBox="0 0 24 24"><circle class="solid" cx="12" cy="12" r="10"/><path d="M2 12h20M12 2c3 3 3 17 0 20M12 2c-3 3-3 17 0 20" stroke="#fff" stroke-width="1.3"/></svg>
        <span>www.meliskaverholt.com</span>
      </li>
      <li>
        <svg viewBox="0 0 24 24"><rect x="3.5" y="3.5" width="17" height="17"/></svg>
        <span>meliskaverholtphotography</span>
      </li>
    </ul>
  </section>

  <section class="card card-back">
    <div class="wash" role="img" aria-label="Soft watercolour wash in cream and sage green"></div>
    <div class="brand">
      <div class="brand-name">Meliska Verholt</div>
      <div class="brand-tag">PHOTOGRAPHY</div>
    </div>
  </section>
</body>
</html>
```